Corvane Tea range - labels for a range of teas.

Our company name is Corvane Tea Company - based in Melbourne, Australia. We have a current logo project with Draft Plaza.

We offer a range of top quality teas - black, green, white, oolongs, herbals, flavoured teas. From Japan, Assam, Darjeeling, Ceylon, Africa and elsewhere. The very best loose teas, and some pyramid tea bags too.

We cover some blends : English Breakfast, African Breakfast, Ceylon Breakfast, Earl Grey amongst them.

And herbal variants: lemon grass and ginger, chamomile, peppermint, rooibos and chilli.

And fruit teas.... and flavoured teas like vanilla, peach and raspberry.

We aim to occupy a modern, contemporary, sophisticated and global space.... but we can be funky too, especially with the fruit and herbal offers. Quality is paramount ! We do not aim to have the biggest range of teas, but we are very particular. And we source directly from origin.... fresh quality teas.

Would lean towards black teas being on a black background label, green teas on a green background, white etas on a white background, herbals maybe on a straw or suitable background, and flavoured teas on a specific background colour too....maybe fuschia? Violet ? But colourful is key.

The panel should indicate teas being Loose or Pyramid bags. And the nett weight should be shown.... Loose could be for example 75 gr, 125 gr 250 gr etc.. And pyramids would show the number of pyramids and weight, example 20 x Pyramids 50 gr
50 Pyramids 150 gr etc.

And 'Corvane Teas' or 'Corvane Tea Company' should be on the panel too. Melbourne can appear as well if it gels with the total look.

There will need to be 2 lines - in order or juxtaposed, doesn't matter - showing the origin and 'mark' and grade. Example being:
Ceylon
Wendrick Pekoe

or

Darjeeling
Morvani TGFOP1

or

China
Jasmine Leaf

We just need templates to cover the different types of tea - black, green, white, herbal, flavoured - as there are too many (and changing) types of tea in the range .

Any questions...please ask...

Thanks

Reason: Needs to have alater deadline than the current Logo Project associated with the same Corvane Tea Company start up.

Target Market(s)

Sophisticated. Real tea lovers. Discriminating tastes.

Weight

Font styles to use
Sans Serif

Requirements
Must have
• Sophisticated
Cool
Premium quality branding
Bold
Uber modern
Nice to have
• BOLD text.....
Cool fonts....
Pretty bold and minimalist - ultra modern if possible....uber modern
Bright colours and use of black and white..... Not really into pastels etc..

Lots of black colour too is a likely plus
Should not have
• Frilly stuff

```html
<!DOCTYPE html>
<html lang="en">
<head>
<meta charset="utf-8">
<title>Corvane Tea Company – Black Tea Labels</title>
<link href="https://fonts.googleapis.com/css2?family=Josefin+Sans:wght@400;600;700&display=swap" rel="stylesheet">
<style>
  :root {
    --page: #ffffff;
    --ink: #000000;
    --header-text: #ffffff;
    --english-light: #6aaaf0;
    --english-mid: #2a80e4;
    --english-deep: #1658d8;
    --african-light: #f36a6a;
    --african-mid: #f2121f;
    --african-warm: #ee7428;
    --earl-light: #c9c9c9;
    --earl-mid: #a9a9a9;
    --earl-deep: #7a7a7a;
  }
  * { box-sizing: border-box; margin: 0; padding: 0; }
  html, body {
    width: 1200px;
    height: 874px;
    overflow: hidden;
    background: var(--page);
  }
  .label-range {
    position: relative;
    width: 1200px;
    height: 874px;
  }
  .tea-label {
    position: absolute;
    top: 136px;
    width: 366px;
    height: 430px;
    overflow: hidden;
    font-family: "Josefin Sans", sans-serif;
    color: var(--ink);
  }
  .tea-label--english { left: 29px; }
  .tea-label--african { left: 413px; }
  .tea-label--earl { left: 798px; }

  .label-header {
    height: 77px;
    background: var(--ink);
    color: var(--header-text);
    display: flex;
    align-items: center;
    justify-content: center;
    padding-top: 12px;
  }
  .company-name {
    font-weight: 400;
    font-size: 28px;
    letter-spacing: -0.5px;
    text-transform: uppercase;
    white-space: nowrap;
  }
  .label-artwork {
    position: absolute;
    top: 77px;
    left: 0;
    width: 100%;
    height: 353px;
  }
  .tea-label--english .label-artwork {
    background: linear-gradient(150deg, var(--english-mid) 0%, var(--english-deep) 35%, var(--english-mid) 55%, var(--english-light) 80%);
  }
  .tea-label--african .label-artwork {
    background: linear-gradient(150deg, var(--african-mid) 0%, var(--african-warm) 35%, var(--african-mid) 60%, var(--african-light) 85%);
  }
  .tea-label--earl .label-artwork {
    background: linear-gradient(150deg, var(--earl-mid) 0%, var(--earl-deep) 35%, var(--earl-mid) 55%, var(--earl-light) 85%);
  }
  .blend-name {
    position: absolute;
    left: 0;
    font-weight: 600;
    font-size: 52px;
    line-height: 54px;
    text-transform: uppercase;
    letter-spacing: -2px;
    white-space: nowrap;
  }
  .blend-name span { display: block; }
  .tea-label--english .blend-name,
  .tea-label--african .blend-name { top: 318px; }
  .tea-label--english .blend-name span:first-child { padding-left: 34px; }
  .tea-label--english .blend-name span:last-child { padding-left: 71px; }
  .tea-label--african .blend-name span:first-child { padding-left: 24px; }
  .tea-label--african .blend-name span:last-child { padding-left: 69px; }
  .tea-label--earl .blend-name {
    top: 338px;
    padding-left: 19px;
    font-size: 48px;
  }
</style>
</head>
<body>
  <main class="label-range">
    <article class="tea-label tea-label--english">
      <header class="label-header"><p class="company-name">Corvane Tea Company</p></header>
      <div class="label-artwork" role="img" aria-label="Abstract flowing brushstroke pattern in layered blues"></div>
      <h2 class="blend-name"><span>English</span><span>Breakfast</span></h2>
    </article>

    <article class="tea-label tea-label--african">
      <header class="label-header"><p class="company-name">Corvane Tea Company</p></header>
      <div class="label-artwork" role="img" aria-label="Abstract flame-like brushstroke pattern in red and orange"></div>
      <h2 class="blend-name"><span>African</span><span>Breakfast</span></h2>
    </article>

    <article class="tea-label tea-label--earl">
      <header class="label-header"><p class="company-name">Corvane Tea Company</p></header>
      <div class="label-artwork" role="img" aria-label="Abstract flowing brushstroke pattern in layered greys"></div>
      <h2 class="blend-name">Earl Grey</h2>
    </article>
  </main>
</body>
</html>
```